Graphic to show easy steps to find financial clarity

Howdy-I need a graphic that describe my Coin Compass Method.The attached is a concept, but please use your own creativity to show how you would display this:- There are 5 steps the process (and then we repeat/recalculate)- And three bullets that drive home the results of the processI've also attached my logo. Please use the colors in my logo and maybe add a soft green as needed.The reader should be able to briefly scan this document and understand that this is an easy/simple process that tells them how to manage their cash.Thanks!-Ned

Target Market(s)

wealthy women, whether single or married

Requirements
Must have
• Please use the colors in my logo and a soft green if needed
Should not have
• This should be a very easy to read graphic that communicates how simple/easy this is to do.

```html
<!DOCTYPE html>
<html lang="en">
<head>
<meta charset="utf-8">
<title>Coin Compass Method</title>
<link rel="stylesheet" href="https://fonts.googleapis.com/css2?family=Montserrat:wght@500;600;700;800&display=swap">
<style>
  :root {
    --navy: #1b4a8a;
    --ink: #1f3d78;
    --green: #8cc63f;
    --icon: #7a7a7a;
    --paper: #ffffff;
  }
  * { box-sizing: border-box; margin: 0; padding: 0; }
  html, body { width: 849px; height: 1200px; overflow: hidden; background: var(--paper); }
  body { font-family: "Montserrat", Arial, sans-serif; color: var(--ink); }
  .poster { position: relative; width: 849px; height: 1200px; }
  .artwork { position: absolute; inset: 0; }

  .brand { position: absolute; left: 0; top: 128px; width: 849px; text-align: center; color: var(--navy); font-weight: 700; font-size: 26px; letter-spacing: 1px; line-height: 1; }

  .title-bar { position: absolute; left: 53px; top: 212px; width: 744px; height: 107px; background: var(--navy); border-radius: 14px; display: flex; align-items: center; justify-content: center; }
  .title { color: var(--green); font-weight: 600; font-size: 50px; letter-spacing: 1px; }

  .step-num { position: absolute; font-weight: 600; color: var(--ink); line-height: 1; font-size: 146px; }
  .step-num.top { top: 344px; }
  .step-num.bottom { top: 618px; }

  .step { position: absolute; width: 176px; background: var(--green); border-radius: 12px; display: flex; flex-direction: column; align-items: center; justify-content: center; text-align: center; line-height: 1.05; }
  .step.top { top: 464px; height: 123px; }
  .step.bottom { top: 738px; height: 125px; }
  .step-label { color: #fff; font-weight: 600; font-size: 15px; margin-bottom: 4px; }
  .step-key { color: var(--ink); font-weight: 700; font-size: 29px; }
  .step-key.huge { font-size: 40px; }
  .step-tail { color: var(--ink); font-weight: 700; font-size: 20px; }

  .results { position: absolute; left: 116px; top: 905px; width: 460px; list-style: none; }
  .results li { position: relative; padding-left: 28px; font-weight: 600; font-size: 18px; line-height: 1.4; margin-bottom: 10px; }
  .results li::before { content: ""; position: absolute; left: 4px; top: 9px; width: 8px; height: 8px; border-radius: 50%; background: var(--ink); }

  .money-art { position: absolute; left: 590px; top: 918px; width: 210px; height: 200px; border-radius: 10px; background: linear-gradient(160deg, #eef2f8, #d6e0ef); }
</style>
</head>
<body>
<div class="poster">
  <svg class="artwork" viewBox="0 0 849 1200" width="849" height="1200" aria-hidden="true">
    <g fill="none" stroke="var(--green)" stroke-width="4" stroke-linecap="round" stroke-linejoin="round">
      <path d="M87 546 H59 V1113 H560"/>
      <path d="M87 818 H59"/>
      <path d="M262 546 H336 M512 546 H580"/>
      <path d="M756 546 H788 V818 H756"/>
      <path d="M580 818 H512 M336 818 H262"/>
      <polyline points="322,538 334,546 322,554"/>
      <polyline points="566,538 578,546 566,554"/>
      <polyline points="780,672 788,684 796,672"/>
      <polyline points="526,810 514,818 526,826"/>
      <polyline points="276,810 264,818 276,826"/>
      <polyline points="51,692 59,680 67,692"/>
      <polyline points="51,950 59,962 67,950"/>
      <polyline points="548,1105 560,1113 548,1121"/>
      <polyline points="350,1105 362,1113 350,1121"/>
    </g>
    <g fill="none" stroke="var(--icon)" stroke-width="2.5" stroke-linejoin="round" stroke-linecap="round">
      <rect x="176" y="368" width="76" height="14" rx="3"/>
      <path d="M188 382 V448 H242 V382"/>
      <text x="215" y="428" font-size="26" text-anchor="middle" fill="var(--icon)" stroke="none" font-family="Montserrat, sans-serif">$</text>
      <rect x="424" y="392" width="84" height="22"/>
      <rect x="432" y="414" width="68" height="42"/>
      <path d="M466 392 V456"/>
      <path d="M466 392 C452 372 436 378 446 390 M466 392 C480 372 496 378 486 390"/>
      <rect x="651" y="364" width="70" height="90" rx="7"/>
      <rect x="661" y="374" width="50" height="18" rx="2"/>
      <path d="M664 410 H680 M672 402 V418 M694 410 H710 M666 426 L678 438 M678 426 L666 438 M694 432 H710"/>
      <circle cx="702" cy="426" r="1.5"/><circle cx="702" cy="438" r="1.5"/>
      <path d="M200 620 H244 V670 H200 Z"/>
      <path d="M210 636 H234 M210 648 H234"/>
      <rect x="180" y="670" width="86" height="52" rx="6"/>
      <path d="M194 686 H252 M194 698 H252"/>
      <path d="M218 712 H228"/>
      <rect x="422" y="632" width="64" height="38" transform="rotate(12 454 651)"/>
      <rect x="440" y="672" width="68" height="40"/>
      <text x="454" y="660" font-size="22" text-anchor="middle" fill="var(--icon)" stroke="none" font-family="Montserrat, sans-serif">$</text>
      <text x="474" y="700" font-size="22" text-anchor="middle" fill="var(--icon)" stroke="none" font-family="Montserrat, sans-serif">€</text>
      <circle cx="690" cy="638" r="17"/>
      <text x="690" y="646" font-size="20" text-anchor="middle" fill="var(--icon)" stroke="none" font-family="Montserrat, sans-serif">$</text>
      <ellipse cx="690" cy="690" rx="44" ry="28"/>
      <path d="M664 714 V726 M714 714 V726 M734 688 C744 688 744 676 736 676"/>
    </g>
  </svg>

  <div class="brand">NORTHVALE WEALTH MANAGEMENT, LLC</div>

  <div class="title-bar"><h1 class="title">COIN COMPASS METHOD</h1></div>

  <span class="step-num top" style="left:100px">1</span>
  <span class="step-num top" style="left:340px">2</span>
  <span class="step-num top" style="left:562px">3</span>
  <span class="step-num bottom" style="left:90px">6</span>
  <span class="step-num bottom" style="left:342px">5</span>
  <span class="step-num bottom" style="left:556px">4</span>

  <div class="step top" style="left:87px"><span class="step-label">KNOW YOUR</span><span class="step-key">ANNUAL<br>SPENDING</span></div>
  <div class="step top" style="left:336px"><span class="step-label">PROJECT</span><span class="step-key">SPECIAL</span><span class="step-tail">EXPENSES</span></div>
  <div class="step top" style="left:580px"><span class="step-label">ADD UP YOUR</span><span class="step-key huge">5-YEAR</span><span class="step-tail">CASH NEEDS</span></div>
  <div class="step bottom" style="left:87px"><span class="step-label">RECALCULATE</span><span class="step-key">MONTHLY</span></div>
  <div class="step bottom" style="left:336px"><span class="step-label">INVEST IN</span><span class="step-key">THE REST</span></div>
  <div class="step bottom" style="left:580px"><span class="step-label">SET THEM</span><span class="step-key huge">ASIDE</span><span class="step-tail">IN SAVINGS</span></div>

  <ul class="results">
    <li>Know your life STYLE WILL BE<br>UNAFFECTED BY the markets<br>for at least 5 years.</li>
    <li>Spend INTENTIONALLY and with JOY.</li>
    <li>Create a solid base for LIFETIME<br>CASH FLOW Projections.</li>
  </ul>

  <div class="money-art" role="img" aria-label="Line drawing of stacked coins and a dollar bill"></div>
</div>
</body>
</html>
```